Marketing Flyer for Plumber Referals

8.5" x11" Layout should be landscape not portrait. Create a bold, eye-catching flyer that highlights earning potential from referrals for water damage restoration. Use high-contrast colors like blue, yellow, and white, with bold fonts and dynamic layouts. Include images of restoration work, cash, and happy clients. Emphasize key benefits like $500 minimum payouts, fast payments, and unlimited income potential. Keep instructions simple: refer a client, we handle the work, you get paid. Add a clear call-to-action and display contact details prominently. Focus on professionalism and energy.

Target Market(s)

Plumbers and Contractor 8.5" x11" Layout should be landscape not portrait.

Industry/Entity Type

General Contractor

Colors
0054AA
0677BA
7BADD7
CADEEF
E8F1F8
EB3D1F
EC4F4E
F09395
F8D3D4
FCEDEE

Requirements
Must have
• 8.5" x11" Layout should be landscape not portrait.
Nice to have

```html
<!DOCTYPE html>
<html lang="en">
<head>
<meta charset="utf-8">
<title>Referral Partner Flyer</title>
<link href="https://fonts.googleapis.com/css2?family=Poppins:wght@300;400;700;800&family=Roboto+Condensed:ital,wght@0,400;0,700;1,700&family=Barlow+Semi+Condensed:wght@500&display=swap" rel="stylesheet">
<style>
  :root{
    --blue:#1656a5;
    --blue-deep:#0054AA;
    --cyan:#1a9bd6;
    --red:#e8402a;
    --red-soft:#EC4F4E;
    --panel:#e6e6ee;
    --sheet:#eef0f4;
    --ink:#ffffff;
    --black:#151515;
  }
  *{margin:0;padding:0;box-sizing:border-box}
  html,body{width:1200px;height:960px;overflow:hidden;background:#fff}
  .flyer{position:relative;width:1200px;height:960px;background:var(--sheet);overflow:hidden;font-family:"Poppins",sans-serif}
  .abs{position:absolute}
  .header-shape{left:0;top:0}
  .headline{left:57px;top:72px;font-size:43px;line-height:44px;letter-spacing:.3px;white-space:nowrap}
  .headline .light{color:var(--red-soft);font-weight:300}
  .headline .bold{color:var(--ink);font-weight:700}
  .cash-photo{left:0;top:194px;width:607px;height:367px;background:linear-gradient(135deg,#d9dde0 0%,#a9b4b8 35%,#7f9498 60%,#c9d0d2 100%)}
  .offer-badge{left:645px;top:85px;width:218px;height:218px;border-radius:50%;background:#fff;text-align:center;color:var(--red);padding-top:30px}
  .offer-badge .amount{font-size:38px;font-weight:700;line-height:40px}
  .offer-badge .amount span{font-weight:400}
  .offer-badge .line{font-size:26px;line-height:28px;font-weight:400}
  .offer-badge .or{font-size:20px;line-height:18px;position:relative;margin:2px 0}
  .offer-badge .or::before,.offer-badge .or::after{content:"";position:absolute;top:10px;width:62px;height:1.5px;background:var(--red)}
  .offer-badge .or::before{left:28px}
  .offer-badge .or::after{right:28px}
  .offer-badge .pct{font-size:38px;line-height:38px;font-weight:400}
  .offer-badge .pct b{font-weight:800}
  .brand-box{left:946px;top:0;width:228px;height:175px;background:var(--black);display:flex;flex-direction:column;align-items:center;justify-content:flex-end;padding-bottom:20px;color:#fff;font-family:"Roboto Condensed",sans-serif;font-weight:400}
  .brand-box .name{font-size:18px;letter-spacing:.8px}
  .brand-box .tag{font-size:7.5px;letter-spacing:2.4px;margin-top:3px}
  .referrals-word{left:646px;top:322px;font-family:"Barlow Semi Condensed",sans-serif;font-weight:500;font-size:84px;letter-spacing:0;color:var(--cyan);line-height:84px;white-space:nowrap}
  .marker-line{left:646px;top:400px}
  .hand-photo{left:880px;top:420px;width:190px;height:141px;border-radius:60px 60px 0 0;background:linear-gradient(160deg,#f0c9ae,#d9a488)}
  .partner{left:652px;top:442px;font-family:"Roboto Condensed",sans-serif}
  .partner .lead{color:var(--red);font-size:18px;line-height:22px}
  .partner .team{color:var(--blue);font-size:23px;font-weight:700;font-style:italic;line-height:28px}
  .flood-photo{left:21px;top:561px;width:372px;height:282px;background:linear-gradient(180deg,#e4e2dc 0%,#b9b2a4 45%,#6f6c66 70%,#3a3a38 100%)}
  .why-title{left:394px;top:566px;width:786px;text-align:center;color:var(--blue);font-size:26px;font-weight:700}
  .benefit{top:609px;height:234px;width:194px;text-align:center;color:#fff;padding-top:10px}
  .benefit.blue{background:var(--blue)}
  .benefit.red{background:var(--red)}
  .benefit svg{display:block;margin:0 auto}
  .benefit h3{font-size:21px;line-height:23px;font-weight:700;margin-top:12px}
  .benefit p{font-family:"Roboto Condensed",sans-serif;font-size:15px;line-height:19px;margin-top:8px;padding:0 6px}
  .slogan{left:0;top:854px;width:1200px;text-align:center;color:var(--blue);font-size:23px;font-weight:700}
  .contact{left:30px;top:890px;height:70px;display:flex;align-items:center;white-space:nowrap}
  .contact .cta{color:var(--blue);font-size:23px;font-weight:700}
  .contact .divider{width:1.5px;height:46px;background:var(--blue);margin:0 10px}
  .contact .phone{color:var(--red);font-size:52px;font-weight:700;letter-spacing:1px;line-height:56px}
  .contact .web{color:var(--blue);font-size:23px;font-weight:700}
</style>
</head>
<body>
<div class="flyer">
  <svg class="abs header-shape" width="1200" height="600" viewBox="0 0 1200 600" aria-hidden="true">
    <rect x="607" y="194" width="593" height="367" fill="#e3e3ec"/>
    <path d="M0 0H1200V194H1040C990 194 975 215 962 240C930 330 860 385 754 385C650 385 590 320 560 250C545 214 530 194 500 194H0Z" fill="#1656a5"/>
  </svg>

  <div class="abs headline">
    <div><span class="light">EARN</span> <span class="bold">UNLIMITED CASH</span></div>
    <div><span class="light">GET PAID TO</span> <span class="bold">REFER A FLOOD</span></div>
  </div>

  <div class="abs cash-photo" role="img" aria-label="Scattered hundred-dollar bills with letter tiles spelling CASH FLOW"></div>

  <div class="abs offer-badge">
    <div class="amount"><span>$</span>500</div>
    <div class="line">Minimum</div>
    <div class="or">or</div>
    <div class="pct"><b>10%</b> Per</div>
    <div class="line">Referral!</div>
  </div>

  <div class="abs brand-box">
    <div class="name">HARBOR CREST BUILDERS</div>
    <div class="tag">COASTAL QUALITY BUILDERS</div>
  </div>

  <div class="abs referrals-word">REFERRALS</div>
  <svg class="abs marker-line" width="400" height="26" viewBox="0 0 400 26" aria-hidden="true">
    <path d="M3 20C110 8 250 4 395 16" stroke="#1a9bd6" stroke-width="5" fill="none" stroke-linecap="round"/>
  </svg>
  <div class="abs hand-photo" role="img" aria-label="Hand holding a blue marker"></div>

  <div class="abs partner">
    <div class="lead">Partner with the</div>
    <div class="team">#1 Water Damage<br>Restoration Team</div>
  </div>

  <div class="abs flood-photo" role="img" aria-label="Flooded home interior with water covering the floor by a staircase"></div>

  <div class="abs why-title">Why Partner with Us?</div>

  <div class="abs benefit blue" style="left:394px">
    <svg width="80" height="96" viewBox="0 0 80 96" fill="none" stroke="#e8402a" stroke-width="3" stroke-linejoin="round">
      <path d="M30 8H52L46 20H36Z"/>
      <circle cx="41" cy="44" r="22"/>
      <text x="41" y="53" text-anchor="middle" font-family="Poppins,sans-serif" font-size="24" font-weight="700" fill="#e8402a" stroke="none">$</text>
      <path d="M4 76L18 66C24 62 30 62 36 64L50 66C54 67 54 72 50 72H38M16 90L26 82H48L74 64C78 62 80 66 77 69L52 88H26"/>
    </svg>
    <h3>Guaranteed<br>Payout</h3>
    <p>Minimum $500 or 10% of the invoice, paid fast.</p>
  </div>

  <div class="abs benefit red" style="left:592px">
    <svg width="80" height="96" viewBox="0 0 80 96" fill="none" stroke="#fff" stroke-width="3" stroke-linejoin="round">
      <rect x="10" y="6" width="54" height="78" rx="2"/>
      <circle cx="37" cy="44" r="17"/>
      <path d="M29 44L35 50L46 38"/>
      <path d="M49 57L66 76"/>
      <path d="M18 72H40M18 78H34"/>
    </svg>
    <h3>Free<br>Evaluations</h3>
    <p>We assess damage and process insurance claims for your clients.</p>
  </div>

  <div class="abs benefit blue" style="left:789px">
    <svg width="80" height="96" viewBox="0 0 80 96" fill="none" stroke="#fff" stroke-width="3" stroke-linejoin="round">
      <circle cx="40" cy="20" r="13"/>
      <path d="M16 66V52C16 42 26 38 40 38C54 38 64 42 64 52V66"/>
      <path d="M40 38V62"/>
      <rect x="6" y="66" width="68" height="20"/>
      <path d="M18 66V86M30 66V86M42 66V86M54 66V86M66 66V86"/>
    </svg>
    <h3>Industry<br>Leaders</h3>
    <p>Certified experts with 24/7 rapid response.</p>
  </div>

  <div class="abs benefit red" style="left:986px">
    <svg width="80" height="96" viewBox="0 0 80 96" fill="none" stroke="#fff" stroke-width="3" stroke-linejoin="round" stroke-linecap="round">
      <path d="M26 24H34C34 16 46 16 46 24H54V34C62 34 62 46 54 46V56H26V46C34 46 34 34 26 34Z"/>
      <path d="M32 56V88M48 56V88"/>
      <path d="M10 20L18 24M70 20L62 24M6 40H16M74 40H64M12 60L20 54M68 60L60 54"/>
    </svg>
    <h3>Affordable<br>Solutions</h3>
    <p>Lowest out-of-pocket costs for your customers.</p>
  </div>

  <div class="abs slogan">Send Referrals. Get Paid. Grow Your Business.</div>

  <div class="abs contact">
    <span class="cta">Call Text or Book on-line</span>
    <span class="divider"></span>
    <span class="phone">555-014-2290</span>
    <span class="divider"></span>
    <span class="web">HarborCrestRemodel.com</span>
  </div>
</div>
</body>
</html>
```